Designing a website that functions as the shop window for the various aspects of my business -...

I need a website, with separate webpages covering the different components of my practice (small animal consultancy, equine behaviour consultancy, legal case work and education provider). I have a website (www.petmindstudio-example.ie) but I haven't updated it in recent years to reflect the newer developments / aspects of my business. Most of my work has been in Ireland but I would like to begin to create an international profile, particularly with regard to the legal casework and offering education within the international horse industry. My overall goal is to improve understanding of animals and animal behaviour, and by doing so, help to reduce the performance of behaviour problems, and also improve animal welfare as a result.

Target Market(s)

Horse and dog owners, horse riders, veterinary surgeons, solicitors

Industry/Entity Type

Legal

Logo Text

Text to be decided on

Number of Pages Required

5+ page

Font styles to use
Sans Serif
Decorative
Script

Colors

Designer to choose colors to be used in the design.

Requirements
Must have
• Relevant content from the attached Flyer including photos
• Use of the phrases:
• 'Understanding Animals'
• Improving animals lives through better understanding
• Science-based, up-to-date relevant information regarding animal behaviour
Nice to have
• 'Leading professional service educating people in understanding animals'
• Separate pages for 1) About, 2) Canine and Feline behaviour Consultancy 3) Equine Consultancy 4) Legal expert witness Consultancy 5) Education 6, FAQs
Should not have
• Prices of services (as these may change from time to time)

```html
<!DOCTYPE html>
<html lang="en">
<head>
<meta charset="utf-8">
<title>PetMind Studio – Understanding Animals</title>
<link href="https://fonts.googleapis.com/css2?family=Kaushan+Script&family=Lato:wght@400;700;900&display=swap" rel="stylesheet">
<style>
:root{
  --green:#0b8a4b;
  --green-dark:#066b39;
  --red:#d5141c;
  --ink:#333;
  --muted:#555;
  --light:#f4f4f4;
  --footer:#1e1f22;
  --white:#fff;
}
*{box-sizing:border-box;margin:0;padding:0}
html,body{width:1200px;height:3974px;overflow:hidden}
body{font-family:'Lato',sans-serif;color:var(--ink);background:var(--white);position:relative}
.abs{position:absolute}
.media{position:absolute;display:block}

/* header */
.topbar{top:0;left:0;width:1200px;height:85px;background:var(--white)}
.phone{left:140px;top:24px;display:flex;align-items:center;gap:14px;font-size:17px;color:var(--ink)}
.round-icon{width:36px;height:36px;border-radius:50%;background:var(--red);display:flex;align-items:center;justify-content:center}
.brand{left:0;width:1200px;top:20px;text-align:center;display:flex;justify-content:center;align-items:center;gap:12px}
.brand-dot{width:30px;height:30px;border-radius:50%;background:var(--green)}
.brand-name{font-family:'Kaushan Script',cursive;font-size:32px;color:var(--green)}
.login{right:140px;top:24px;display:flex;align-items:center;gap:14px;font-size:17px}
.nav{top:85px;left:0;width:1200px;height:34px;background:var(--green)}
.nav ul{list-style:none;display:flex;position:absolute;left:140px;top:0;height:34px}
.nav li{color:var(--white);font-size:14px;padding:0 20px;line-height:34px}
.nav li.active{background:var(--green-dark);font-weight:700}
.cta-btn{right:140px;top:0;height:34px;line-height:34px;padding:0 18px;background:var(--green-dark);color:var(--white);font-size:14px;font-weight:700}

/* hero */
.hero{top:119px;left:0;width:1200px;height:511px;background:linear-gradient(90deg,#dfe5dc 0%,#c9d2c3 45%,#8a5a33 70%,#6f4323 100%)}
.hero h1{position:absolute;left:142px;top:168px;font-family:'Kaushan Script',cursive;font-weight:400;font-size:44px;line-height:56px;color:var(--green)}
.hero h1 .red{color:var(--red)}

/* about */
.about{top:630px;left:0;width:1200px;height:415px;background:linear-gradient(180deg,#f2f2f2,#fff)}
.about .media{left:53px;top:25px;width:503px;height:390px;background:linear-gradient(135deg,#e9e6e2,#cfc9c2 55%,#f3f3f3)}
.section-title{font-family:'Kaushan Script',cursive;font-weight:400;color:var(--green);font-size:26px;display:flex;align-items:center;gap:10px}
.title-mark{width:22px;height:22px;border-radius:50%;background:var(--green);display:inline-block}
.about .section-title{position:absolute;left:612px;top:78px}
.about .sub{position:absolute;left:612px;top:130px;color:var(--red);font-weight:700;font-size:15px}
.about p{position:absolute;left:612px;top:160px;width:445px;font-size:13.5px;line-height:21px;color:var(--muted)}
.btn{display:inline-block;background:var(--green);color:var(--white);font-weight:700;font-size:13px;padding:11px 24px;border-radius:3px;text-transform:uppercase}
.about .btn{position:absolute;left:618px;top:300px}

/* offer */
.offer{top:1045px;left:0;width:1200px;height:518px;background:var(--white)}
.offer .section-title{position:absolute;left:0;width:1200px;justify-content:center;top:100px}
.tabs{position:absolute;left:140px;top:180px;width:222px;border-right:1px solid #ddd;text-align:right}
.tabs li{list-style:none;font-size:14px;line-height:41px;padding-right:20px;color:var(--muted)}
.tabs li.on{color:var(--green);font-weight:700;border:1px solid #ccc;margin-left:10px;background:#fafafa}
.offer-text{position:absolute;left:382px;top:180px;width:385px;font-size:13.5px;line-height:23px;color:var(--muted)}
.offer-text p+p{margin-top:12px}
.offer .media{left:790px;top:120px;width:300px;height:305px;background:linear-gradient(160deg,#fff,#e8dccb 40%,#8b6a45 75%,#fff)}

/* bands */
.band{left:0;width:1200px;text-align:center;color:var(--white);font-family:'Kaushan Script',cursive;font-size:28px}
.band-green1{top:1563px;height:165px;background:var(--green)}
.band-green1 span{position:absolute;left:380px;top:62px}
.band-green1 .media{left:80px;top:-30px;width:270px;height:190px;background:linear-gradient(180deg,#e7d7bf,#b79973)}
.band-red{top:2883px;height:159px;background:var(--red);line-height:42px}
.band-red .text{position:absolute;left:0;width:1200px;top:38px}
.band-red .media{left:905px;top:-60px;width:200px;height:219px;background:linear-gradient(180deg,#a77a55,#5f3c22)}
.band-green2{top:3511px;height:164px;background:var(--green);line-height:42px}
.band-green2 .text{position:absolute;left:0;width:1200px;top:38px}

/* services */
.services{top:1728px;left:0;width:1200px;height:596px;background:linear-gradient(90deg,#24201b,#3d3127 50%,#221e1a)}
.services .section-title{position:absolute;left:0;width:1200px;justify-content:center;top:90px;color:var(--white)}
.services .title-mark{background:var(--white)}
.card{position:absolute;top:162px;width:285px;height:342px;background:var(--white);text-align:center}
.card .media{position:relative;width:285px;height:172px}
.card h3{font-size:15px;font-weight:700;line-height:21px;margin-top:16px;color:#222}
.card p{font-size:12.5px;line-height:18px;color:var(--muted);padding:8px 30px 0}
.plus{position:absolute;left:122px;bottom:-20px;width:40px;height:40px;border-radius:50%;background:var(--green);color:var(--white);font-size:24px;line-height:38px;font-weight:700}

/* reviews */
.reviews{top:2324px;left:0;width:1200px;height:559px;background:var(--white)}
.reviews .section-title{position:absolute;left:0;width:1200px;justify-content:center;top:82px}
.reviews .media{left:140px;top:154px;width:332px;height:305px;background:linear-gradient(135deg,#e6d6bf,#c59a62 50%,#8b5e34)}
.quote{position:absolute;left:510px;top:158px;width:548px;font-size:13px;line-height:20.5px;color:var(--muted)}
.quote .mark{color:var(--green);font-size:26px;font-family:'Kaushan Script',cursive;line-height:10px}
.reviewer{position:absolute;left:510px;top:356px;font-size:13px;line-height:21px}
.reviewer b{color:var(--green)}
.view-all{position:absolute;left:508px;top:420px}

/* inquiry */
.inquiry{top:3042px;left:0;width:1200px;height:469px;background:linear-gradient(180deg,#6f7f93 0%,#d6a064 48%,#6b6a3a 75%,#3f5a2a 100%)}
.form{position:absolute;left:657px;top:96px;width:400px}
.form h2{font-family:'Kaushan Script',cursive;font-weight:400;color:var(--green);font-size:26px;display:flex;align-items:center;gap:10px}
.form .lead{color:var(--white);font-size:13px;margin:10px 0 12px}
.field{background:rgba(255,255,255,.92);height:32px;font-size:12px;color:#777;padding:0 10px;line-height:32px}
.row{display:flex;gap:12px;margin-bottom:12px}
.row .field{flex:1}
.msg{height:44px;margin-bottom:14px}
.form .btn{padding:10px 38px}

/* footer */
.footer{top:3675px;left:0;width:1200px;height:265px;background:var(--footer);color:#ccc}
.fcol{position:absolute;top:48px;font-size:12.5px;line-height:21px}
.fcol h4{font-size:14px;color:var(--white);font-weight:700;margin-bottom:8px;text-transform:uppercase}
.fcol h4 span{color:var(--green)}
.fcol ul{list-style:none}
.fcol li::before{content:"› ";color:var(--green)}
.contact-line{display:flex;gap:10px;margin-bottom:10px;align-items:flex-start}
.contact-line .ic{width:14px;height:14px;flex:none;margin-top:3px}
.social li{list-style:none;display:flex;align-items:center;gap:10px;margin-bottom:8px}
.social li::before{content:none}
.sdot{width:24px;height:24px;border-radius:50%;display:inline-block}
.hours{font-size:12px;border-collapse:collapse}
.hours td{padding:1px 0;color:#ccc}
.hours td:first-child{width:120px}
.copyright{top:3940px;left:0;width:1200px;height:34px;background:var(--green);color:var(--white);font-size:11px;text-align:center;line-height:34px}
</style>
</head>
<body>

<header class="abs topbar">
  <div class="abs phone"><span class="round-icon"><svg width="16" height="16" viewBox="0 0 24 24"><path fill="#fff" d="M6.6 10.8a15 15 0 0 0 6.6 6.6l2.2-2.2c.3-.3.7-.4 1-.2 1.1.4 2.3.6 3.6.6.6 0 1 .4 1 1V20c0 .6-.4 1-1 1A17 17 0 0 1 3 4c0-.6.4-1 1-1h3.5c.6 0 1 .4 1 1 0 1.3.2 2.5.6 3.6.1.3 0 .7-.2 1z"/></svg></span>087 555 0142</div>
  <div class="abs brand"><span class="brand-dot"></span><span class="brand-name">PetMind Studio</span></div>
  <div class="abs login"><span class="round-icon"><svg width="16" height="16" viewBox="0 0 24 24"><path fill="none" stroke="#fff" stroke-width="2.4" d="M10 7l5 5-5 5M3 12h12M14 4h6v16h-6"/></svg></span>Login</div>
</header>

<nav class="abs nav">
  <ul><li class="active">Home</li><li>About Us</li><li>Behaviour Problems</li><li>Consultations</li><li>Clinics</li><li>Contact Us</li></ul>
  <div class="abs cta-btn">Schedule A Consultation</div>
</nav>

<section class="abs hero">
  <div class="media" style="inset:0" role="img" aria-label="Two bridled chestnut horses standing together in front of a paddock and farm building"></div>
  <h1>Our Goal Is To Improve<br>Understanding of Animals<br><span class="red">&amp; Animal Behavior</span></h1>
</section>

<section class="abs about">
  <div class="media" role="img" aria-label="Young rider in a helmet beside a grey horse's head"></div>
  <h2 class="section-title"><span class="title-mark"></span>About PetMind Studio</h2>
  <div class="sub">Equine Training, Performance and Welfare</div>
  <p>The PetMind Studio was established in 1994 by Maeve Carrick as an animal behaviour referral, consultancy and education provider dedicated to improving understanding of animal behaviour and welfare and investigating and resolving problem behaviours in a range of animal species. Maeve Carrick grew up on a quiet peninsula in the north-west.</p>
  <span class="btn">Read More</span>
</section>

<section class="abs offer">
  <h2 class="section-title"><span class="title-mark"></span>What We offer</h2>
  <ul class="tabs">
    <li class="on">Training Sessions</li>
    <li>Behaviour Consultations</li>
    <li>Training, Performance &amp; Welfare</li>
    <li>Training Your Horse</li>
  </ul>
  <div class="offer-text">
    <p>During a behaviour consultation, an individual assessment of the horse is carried out, incorporating information regarding the horses health, management, past training and competition history, current training methods and outcomes, behaviour patterns displayed, problem behaviours or simply poor performance.</p>
    <p>Recommendations are made at the end of each consultation regarding management, training etc, required to achieve the desired outcome.</p>
  </div>
  <div class="media" role="img" aria-label="Woman crouching with two brown dogs"></div>
</section>

<section class="abs band band-green1">
  <div class="media" role="img" aria-label="Bulldog resting over the top edge of the band"></div>
  <span>Improving Animals Lives Through Better Understanding</span>
</section>

<section class="abs services">
  <h2 class="section-title"><span class="title-mark"></span>Our Services</h2>
  <article class="card" style="left:140px">
    <div class="media" style="background:linear-gradient(135deg,#cdb79a,#8b6a4a)" role="img" aria-label="Woman greeting a small dog"></div>
    <h3>Canine And Feline<br>Behaviour Consultancy</h3>
    <p>Lorem ipsum dolor sit amet, consectetuer adipiscing elit, sed diam nonummy nibh euismod tincidunt ut laoreet dolore</p>
    <div class="plus">+</div>
  </article>
  <article class="card" style="left:457px">
    <div class="media" style="background:linear-gradient(135deg,#6a5d55,#b34a5a 55%,#3d3a3a)" role="img" aria-label="Two women with a horse in a stable"></div>
    <h3>Equine<br>Consultancy</h3>
    <p>Lorem ipsum dolor sit amet, consectetuer adipiscing elit, sed diam nonummy nibh euismod tincidunt ut laoreet dolore</p>
    <div class="plus">+</div>
  </article>
  <article class="card" style="left:775px">
    <div class="media" style="background:linear-gradient(135deg,#d9c3a0,#8a6840 50%,#2f2a28)" role="img" aria-label="Professionals in a legal office meeting"></div>
    <h3>Legal Expert Witness<br>Consultancy</h3>
    <p>Lorem ipsum dolor sit amet, consectetuer adipiscing elit, sed diam nonummy nibh euismod tincidunt ut laoreet dolore</p>
    <div class="plus">+</div>
  </article>
</section>

<section class="abs reviews">
  <h2 class="section-title"><span class="title-mark"></span>Happy Customer Reviews</h2>
  <div class="media" role="img" aria-label="Smiling woman hugging a large dog"></div>
  <blockquote class="quote"><span class="mark">“</span> Dr Maeve Carrick is an outstanding practitioner of Equitation Science and I am very enthusiastic to support her in establishing Equitation Science in Ireland. Aside from her credentials and noteworthy academic publications in Equitation Science, Maeve also has the distinct advantage of being a qualified veterinary behaviourist with an established practice at a national university and also as a behavioural consultant to a city zoo. In that regard, from a multi-species and multidisciplinary standpoint, Maeve has a highly accomplished and unique background that is complemented by her lifetime experience with horses in training and competition horse trials’. <span class="mark">”</span></blockquote>
  <div class="reviewer"><b>Dr Samuel Brennan,</b><br>Equine Learning Institute, Australia.</div>
  <span class="btn view-all">View All</span>
</section>

<section class="abs band band-red">
  <div class="text">Science-based, Up-to-date Relevant Information<br>Regarding Animal Behaviour</div>
  <div class="media" role="img" aria-label="Chestnut horse head looking over the band"></div>
</section>

<section class="abs inquiry">
  <div class="media" style="inset:0;background:transparent" role="img" aria-label="Sunset field scene with a saddled horse, a rider and a black dog"></div>
  <div class="form">
    <h2><span class="title-mark"></span>Quick Inquiry</h2>
    <p class="lead">Lorem ipsum dolor sit amet, consectetuer adipiscing elit, sed diam</p>
    <div class="row"><div class="field">First Name</div><div class="field">Last Name</div></div>
    <div class="row"><div class="field">Email</div><div class="field">Phone Number</div></div>
    <div class="field msg">Message</div>
    <span class="btn">Submit</span>
  </div>
</section>

<section class="abs band band-green2">
  <div class="text">Leading Professional Service Educating People<br>In Understanding Animals</div>
</section>

<footer class="abs footer">
  <div class="fcol" style="left:145px">
    <h4>Quick <span>Links</span></h4>
    <ul><li>Home</li><li>About Us</li><li>Behaviour Problems</li><li>Consultations</li><li>Clinics</li><li>Contact Us</li><li>Sitemap</li></ul>
  </div>
  <div class="fcol" style="left:322px;width:250px">
    <h4>Contact <span>Details</span></h4>
    <div class="contact-line"><svg class="ic" viewBox="0 0 24 24"><path fill="#0b8a4b" d="M12 2a7 7 0 0 0-7 7c0 5 7 13 7 13s7-8 7-13a7 7 0 0 0-7-7zm0 9.5A2.5 2.5 0 1 1 12 6.5a2.5 2.5 0 0 1 0 5z"/></svg><span><span style="color:#0b8a4b">PetMind Studio</span><br>1234 Lorem Road, Suite 123 Fort<br>ABB 123456</span></div>
    <div class="contact-line"><svg class="ic" viewBox="0 0 24 24"><path fill="#0b8a4b" d="M6.6 10.8a15 15 0 0 0 6.6 6.6l2.2-2.2c.3-.3.7-.4 1-.2 1.1.4 2.3.6 3.6.6.6 0 1 .4 1 1V20c0 .6-.4 1-1 1A17 17 0 0 1 3 4c0-.6.4-1 1-1h3.5c.6 0 1 .4 1 1 0 1.3.2 2.5.6 3.6.1.3 0 .7-.2 1z"/></svg><span>087 555 0142</span></div>
    <div class="contact-line"><svg class="ic" viewBox="0 0 24 24"><path fill="#0b8a4b" d="M3 5h18v14H3zm2 2v.5l7 5 7-5V7z"/></svg><span>hello@petmindstudio-example.ie</span></div>
  </div>
  <div class="fcol social" style="left:590px">
    <h4>Follow <span>Us</span></h4>
    <ul>
      <li><span class="sdot" style="background:#c41a1a"></span>Reviews</li>
      <li><span class="sdot" style="background:#2f5fa8"></span>Community</li>
      <li><span class="sdot" style="background:#2aa3e0"></span>Updates</li>
      <li><span class="sdot" style="background:#d61f1f"></span>Videos</li>
    </ul>
  </div>
  <div class="fcol" style="left:805px">
    <h4>Opening <span>Hours</span></h4>
    <table class="hours">
      <tr><td>Monday</td><td>9:30 am&nbsp;&nbsp;–&nbsp;&nbsp;6:00 pm</td></tr>
      <tr><td>Tuesday</td><td>9:30 am&nbsp;&nbsp;–&nbsp;&nbsp;6:00 pm</td></tr>
      <tr><td>Wednesday</td><td>9:30 am&nbsp;&nbsp;–&nbsp;&nbsp;6:00 pm</td></tr>
      <tr><td>Thursday</td><td>9:30 am&nbsp;&nbsp;–&nbsp;&nbsp;6:00 pm</td></tr>
      <tr><td>Friday</td><td>9:30 am&nbsp;&nbsp;–&nbsp;&nbsp;6:00 pm</td></tr>
      <tr><td>Saturday &amp; Sunday</td><td>Off</td></tr>
    </table>
  </div>
</footer>
<div class="abs copyright">Copyright © 2019 PetMind Studio. All Rights Reserved.</div>

</body>
</html>
```